Maple Roadway Handbook
2nd Edition
Love #26 and #28 and #33
The graphics are original, they don't make it appear as if I am promoting Driving drunk and they have good graphic appeal.
I don't want to seem like I am promoting Driving drunk so #32 (and #19 and #29)seem to dance a little too close to the edge.
#25 -Awesome job! I need you to post a version with
1) No text on the back cover
2) No publisher's logo and location
3) No ISBN number or bar code
3) No photo (leave the white box under neath the photo)
4) No text on the spine
I like that this cover is implementing a graphic of some sort (the swirly thingy). I am not wild about brown though.
I would recommend getting rid of the glow around the subtext and the underline on the very top. However, I don't know that I would choose this design idea even if it was executed perfectly.
Take your designs in a whole new direction. The fonts and text locations are easy to tweak, the hard part is thinking of a unique graphic to make the focus of the cover. Most of the submissions so far have implement text and colored rectangles, so try to think of a stock photo or a graphic or a shape that will grab the attention, and then worry about the text later.
I am hoping for someone to submit designs that implement graphics, photos, or something more than a few two-toned rectangles.
#6 and #7 are nearly exact copies of the first edition only the color is changed slightly. I will not choose a submission that is essentially a version of the first edition.
#5 This is almost an exact replica of the first edition only its blue. I am not interested in designs that look similar to the first edition.
#3 The big gold start is not a wholly bad element, but I think having it front and center, makes it too prominent.
General Comment.
The Back cover of this book will have:
1) an ISBN
2)Text
3) A photo
4)the publishers logo
HOWEVER - The design we choose will not have any of those elements included. We will be altering the photo, text, ect. and pasting then on top of the design chosen here.
I think it is really helpful to include some place holder, text, photos, isbn ect. on your initial submissions so we can see how the elements will fit into your back cover layout, but once we have zeroed in on a design we like, we will need to have those elements removed.
#2 and #3 I am not wild about the colors.
#1 The title font is a bit cartoonist, which doesn't work well for a law firm trying to impress clientele. Also, all the text is crammed into the top of the cover, leaving a large blank space in the bottom 2/3.
I would reexamine your font selection. take a look at some professional text books and reference books. I would also consider how to balance the test at the top with the emptiness at the bottom. Once again, take a look at other professional text and reference books for ideas.
#4 I like the the colors and the different color blocks, but I am not wild about the word "Handbook" written vertically. I feel like something should be written there, but I am not sure about what, and the word "handbook" is not something that is particularly important or deserves emphasis.
Submissions #4,3,& 2 I appreciate you doing a mock up of the back page, but the your final submission should not have the text, picture, publisher's logo, or the ISBN. All of those items will be pasted ontop of your submission after the fact. You can go ahead an add them just so I can see what it would look like, but final submission would need to be altered.

```html
<!DOCTYPE html>
<html lang="en">
<head>
<meta charset="utf-8">
<title>The Maple Roadway Handbook – Cover</title>
<link rel="stylesheet" href="https://fonts.googleapis.com/css2?family=Anton&family=Oswald:wght@500;700&display=swap">
<style>
  :root {
    --stage: #5e5e5e;
    --stage-dark: #3c3c3c;
    --cover-dark: #231f1f;
    --cover-mid: #4a4444;
    --accent: #ffe800;
    --paper: #ffffff;
    --text-light: #f4f4f4;
    --crop: #d8d8d8;
  }
  html, body {
    margin: 0;
    width: 1200px;
    height: 826px;
    overflow: hidden;
  }
  body {
    background: radial-gradient(ellipse at center, var(--stage) 0%, var(--stage-dark) 100%);
    position: relative;
    font-family: "Oswald", "Arial Narrow", sans-serif;
  }
  .crop-marks {
    position: absolute;
    inset: 0;
  }
  .cover {
    position: absolute;
    left: 149px;
    top: 91px;
    width: 907px;
    height: 641px;
    overflow: hidden;
    background: radial-gradient(ellipse at 62% 45%, var(--cover-mid) 0%, var(--cover-dark) 75%);
  }
  .top-band {
    position: absolute;
    left: 0;
    top: 58px;
    width: 100%;
    height: 38px;
    background: var(--accent);
  }
  .photo-slot {
    position: absolute;
    left: 266px;
    top: 70px;
    width: 125px;
    height: 168px;
    background: var(--paper);
  }
  .corner-block {
    position: absolute;
    left: 0;
    bottom: 0;
    width: 228px;
    height: 96px;
    background: var(--accent);
  }
  .title {
    position: absolute;
    right: 22px;
    top: 20px;
    width: 260px;
    text-align: right;
    margin: 0;
    font-weight: normal;
    line-height: 1;
    text-transform: uppercase;
  }
  .title-the {
    display: block;
    font-family: "Anton", "Impact", sans-serif;
    font-size: 28px;
    color: var(--text-light);
    letter-spacing: 1px;
  }
  .title-place {
    display: block;
    font-family: "Anton", "Impact", sans-serif;
    font-size: 36px;
    color: var(--cover-dark);
    height: 38px;
    line-height: 38px;
    margin-top: 6px;
    letter-spacing: 1px;
  }
  .title-main {
    display: block;
    font-family: "Anton", "Impact", sans-serif;
    font-size: 66px;
    color: var(--accent);
    margin-top: 6px;
    letter-spacing: 1px;
  }
  .title-book {
    display: block;
    font-family: "Anton", "Impact", sans-serif;
    font-size: 34px;
    color: var(--text-light);
    margin-top: 6px;
    letter-spacing: 1px;
  }
  .edition {
    display: block;
    font-family: "Oswald", "Arial Narrow", sans-serif;
    font-weight: 700;
    font-size: 15px;
    color: var(--text-light);
    margin-top: 2px;
    letter-spacing: 0.5px;
  }
  .feature-art {
    position: absolute;
    left: 535px;
    top: 150px;
    width: 310px;
    height: 480px;
    background: radial-gradient(ellipse at 40% 70%, #d9c56a 0%, #bfbfbf 30%, #7c7a78 60%, rgba(74,68,68,0) 80%);
  }
  .subtitle {
    position: absolute;
    right: 22px;
    top: 300px;
    width: 210px;
    margin: 0;
    text-align: right;
    color: var(--text-light);
    font-weight: 700;
    line-height: 1.1;
  }
  .subtitle .lead {
    display: block;
    font-size: 22px;
  }
  .subtitle .rest {
    display: block;
    font-size: 15.5px;
  }
  .subtitle .close {
    display: block;
    font-size: 22px;
  }
  .author {
    position: absolute;
    right: 22px;
    bottom: 34px;
    margin: 0;
    color: var(--text-light);
    font-weight: 700;
    font-size: 20px;
  }
</style>
</head>
<body>
  <svg class="crop-marks" width="1200" height="826" aria-hidden="true">
    <g stroke="var(--crop)" stroke-width="1.5">
      <line x1="120" y1="91" x2="140" y2="91"/>
      <line x1="149" y1="62" x2="149" y2="82"/>
      <line x1="1065" y1="91" x2="1085" y2="91"/>
      <line x1="1056" y1="62" x2="1056" y2="82"/>
      <line x1="120" y1="732" x2="140" y2="732"/>
      <line x1="149" y1="741" x2="149" y2="761"/>
      <line x1="1065" y1="732" x2="1085" y2="732"/>
      <line x1="1056" y1="741" x2="1056" y2="761"/>
      <line x1="602" y1="62" x2="602" y2="82"/>
      <line x1="602" y1="741" x2="602" y2="761"/>
    </g>
  </svg>

  <main class="cover">
    <div class="top-band"></div>
    <div class="photo-slot"></div>
    <div class="corner-block"></div>

    <div class="feature-art" role="img" aria-label="Photo of a beer glass with car keys resting on the rim and a pair of handcuffs beside it"></div>

    <h1 class="title">
      <span class="title-the">The</span>
      <span class="title-place">Maple</span>
      <span class="title-main">Roadway</span>
      <span class="title-book">Handbook</span>
      <span class="edition">Second Edition</span>
    </h1>

    <p class="subtitle">
      <span class="lead">Answers to 14</span>
      <span class="rest">Common Questions<br>and Everything Else<br>You Need to Know</span>
      <span class="close">About DUIs</span>
    </p>

    <p class="author">Daniel R. Fenwick</p>
  </main>
</body>
</html>
```